Cedarline Residences —-

Letter head for my apartment building of 15 Floors
In Kampala, Uganda

CEDARLINE RESIDENCIES
14 KIVARA RIDGE ROAD
ASHVALE - LORENTA
P.O. BOX 38516
LORENTA— EASTMARCH

```html
<!DOCTYPE html>
<html lang="en">
<head>
<meta charset="utf-8">
<title>Cedarline Residences — Letterhead</title>
<link rel="stylesheet" href="https://fonts.googleapis.com/css2?family=Montserrat:wght@400;700&display=swap">
<style>
  :root {
    --backdrop: #e6e6e6;
    --paper: #ffffff;
    --charcoal: #3b3b3d;
    --steel: #6e6e72;
    --amber: #f0922b;
    --ink: #2b2b2b;
    --ink-soft: #6a6a6a;
  }
  * { box-sizing: border-box; margin: 0; padding: 0; }
  html, body {
    width: 1200px; height: 1003px; overflow: hidden;
    background: var(--backdrop);
  }
  .letterhead {
    position: absolute;
    left: 267px; top: 31px;
    width: 666px; height: 941px;
    background: var(--paper);
    box-shadow: 0 6px 24px rgba(0,0,0,0.12);
  }
  .letterhead__header {
    position: absolute; left: 0; top: 0; right: 0;
    height: 148px;
    background: var(--charcoal);
  }
  .brand-name {
    position: absolute; left: 128px; top: 64px;
    font-family: "Montserrat", Arial, sans-serif;
    font-weight: 400;
    font-size: 20px; letter-spacing: 3px; line-height: 1;
    color: var(--paper);
    white-space: nowrap;
  }
  .header-rule--amber {
    position: absolute; left: 68px; top: 144px;
    width: 250px; height: 4px; background: var(--amber);
  }
  .header-rule--steel {
    position: absolute; left: 318px; top: 140px;
    width: 330px; height: 4px; background: var(--steel);
  }
  .letterhead__footer {
    position: absolute; left: 0; right: 0; bottom: 0; height: 120px;
  }
  .address {
    position: absolute; left: 66px; top: 22px;
    font-family: "Montserrat", Arial, sans-serif;
    font-size: 11px; letter-spacing: 0.6px; line-height: 1.35;
    color: var(--ink-soft);
  }
  .address__block {
    display: flex; align-items: center; gap: 8px;
  }
  .address__lines {
    padding: 3px 0 4px;
    border-bottom: 1px solid var(--ink-soft);
    width: 160px;
    white-space: nowrap;
  }
  .address__lines--post { border-bottom: none; }
  .address__country {
    font-weight: 700; color: var(--ink); letter-spacing: 0.8px;
  }
  .address__icon { width: 12px; height: 12px; flex: none; }
  .footer-band {
    position: absolute; left: 0; right: 0; bottom: 0;
    height: 9px; background: var(--amber);
  }
</style>
</head>
<body>
  <main class="letterhead">
    <header class="letterhead__header">
      <div class="brand-name">CEDARLINE RESIDENCIES</div>
      <div class="header-rule--steel"></div>
      <div class="header-rule--amber"></div>
    </header>

    <footer class="letterhead__footer">
      <div class="address">
        <div class="address__block">
          <svg class="address__icon" viewBox="0 0 12 12" aria-hidden="true">
            <path d="M6 1a3 3 0 0 1 3 3c0 2.2-3 5-3 5S3 6.2 3 4a3 3 0 0 1 3-3z" fill="none" stroke="#f0922b" stroke-width="1.3"/>
            <circle cx="6" cy="4" r="1" fill="#f0922b"/>
            <path d="M2 11h8" stroke="#f0922b" stroke-width="1.3"/>
          </svg>
          <div class="address__lines">14 KIVARA RIDGE ROAD<br>ASHVALE - LORENTA</div>
        </div>
        <div class="address__block">
          <svg class="address__icon" viewBox="0 0 12 12" aria-hidden="true">
            <rect x="1.5" y="4" width="9" height="5" rx="1.5" fill="none" stroke="#f0922b" stroke-width="1.2"/>
            <path d="M6 9v2.5M8 4V1.5h2" fill="none" stroke="#f0922b" stroke-width="1.2"/>
          </svg>
          <div class="address__lines address__lines--post">P.O. BOX 38516<br><span class="address__country">LORENTA— EASTMARCH</span></div>
        </div>
      </div>
      <div class="footer-band"></div>
    </footer>
  </main>
</body>
</html>
```